Business Card Design

New business card design

Target Market(s)

Residential & Commercial Property Managers

Industry/Entity Type

Plumbing Services

Contact Information for Business Card

Name - Owen Tredgold, title - Director, Phone Number - 0431 862 507, email - owen@rvb-plumbing.com.au, Company ABN - 73 215 904 386,

Font styles to use
Sans Serif

Colors
0054AA
0677BA
7BADD7
CADEEF
E8F1F8

```html
<!DOCTYPE html>
<html lang="en">
<head>
<meta charset="utf-8">
<title>RVB Plumbing Services – Business Card</title>
<link href="https://fonts.googleapis.com/css2?family=Lato:wght@400;700;900&display=swap" rel="stylesheet">
<style>
  :root {
    --page-bg: #2b2d31;
    --card-bg: #1f242b;
    --accent: #0e9be6;
    --accent-deep: #0677ba;
    --text-light: #f2f4f6;
    --text-muted: #aab4bf;
    --divider: #39414b;
  }
  * { margin: 0; padding: 0; box-sizing: border-box; }
  html, body { width: 1200px; height: 952px; overflow: hidden; }
  body {
    background: var(--page-bg);
    font-family: "Lato", sans-serif;
    display: flex;
    align-items: center;
    justify-content: center;
    gap: 40px;
  }
  .card {
    position: relative;
    width: 540px;
    height: 330px;
    background: var(--card-bg);
    overflow: hidden;
    box-shadow: 0 14px 30px rgba(0,0,0,0.35);
  }
  .card__rule {
    position: absolute;
    top: 0;
    bottom: 0;
    left: 56px;
    width: 2px;
    background: var(--accent);
  }
  .brand {
    position: absolute;
    left: 58px;
    right: 0;
    display: flex;
    align-items: center;
    justify-content: center;
    gap: 10px;
  }
  .brand__dot {
    width: 12px;
    height: 12px;
    border-radius: 50%;
    background: var(--accent);
  }
  .brand__name {
    color: var(--text-light);
    font-weight: 700;
    font-size: 30px;
    letter-spacing: 1px;
    white-space: nowrap;
  }
  .card--front .brand { top: 142px; }
  .card--back .brand { top: 70px; }
  .person {
    position: absolute;
    top: 158px;
    left: 76px;
    width: 172px;
    text-align: right;
  }
  .person__name {
    color: var(--accent);
    font-size: 19px;
    font-weight: 400;
    letter-spacing: 0.5px;
    text-transform: uppercase;
    white-space: nowrap;
  }
  .person__name strong { font-weight: 900; }
  .person__title {
    color: var(--text-muted);
    font-size: 13px;
    margin-top: 4px;
  }
  .card__divider {
    position: absolute;
    left: 260px;
    top: 150px;
    width: 1px;
    height: 68px;
    background: var(--divider);
  }
  .contact {
    position: absolute;
    left: 274px;
    top: 158px;
    list-style: none;
  }
  .contact__item {
    display: flex;
    align-items: center;
    gap: 8px;
    color: var(--text-light);
    font-size: 13px;
    height: 24px;
    white-space: nowrap;
  }
  .contact__icon {
    width: 16px;
    height: 16px;
    border-radius: 3px;
    background: var(--accent);
    display: flex;
    align-items: center;
    justify-content: center;
  }
  .abn {
    position: absolute;
    left: 240px;
    top: 232px;
    font-size: 15px;
    color: var(--text-light);
    white-space: nowrap;
  }
  .abn__label { color: var(--accent); }
</style>
</head>
<body>
  <section class="card card--front" aria-label="Card front">
    <div class="card__rule"></div>
    <div class="brand">
      <span class="brand__dot"></span>
      <span class="brand__name">RVB Plumbing Services</span>
    </div>
  </section>

  <section class="card card--back" aria-label="Card back">
    <div class="card__rule"></div>
    <div class="brand">
      <span class="brand__dot"></span>
      <span class="brand__name">RVB Plumbing Services</span>
    </div>
    <div class="person">
      <p class="person__name">Owen <strong>Tredgold</strong></p>
      <p class="person__title">Director</p>
    </div>
    <div class="card__divider"></div>
    <ul class="contact">
      <li class="contact__item">
        <span class="contact__icon">
          <svg width="10" height="10" viewBox="0 0 24 24" aria-hidden="true"><path fill="#1f242b" d="M6.6 10.8a15.1 15.1 0 0 0 6.6 6.6l2.2-2.2c.3-.3.7-.4 1-.2 1.1.4 2.3.6 3.6.6.6 0 1 .4 1 1V20c0 .6-.4 1-1 1A17 17 0 0 1 3 4c0-.6.4-1 1-1h3.5c.6 0 1 .4 1 1 0 1.3.2 2.5.6 3.6.1.3 0 .7-.2 1z"/></svg>
        </span>
        0431 862 507
      </li>
      <li class="contact__item">
        <span class="contact__icon">
          <svg width="10" height="10" viewBox="0 0 24 24" aria-hidden="true"><path fill="none" stroke="#1f242b" stroke-width="2.5" d="M3 6h18v12H3z M3 6l9 7 9-7"/></svg>
        </span>
        owen@rvb-plumbing.com.au
      </li>
    </ul>
    <p class="abn"><span class="abn__label">ABN -</span> 73 215 904 386</p>
  </section>
</body>
</html>
```